Flitterhorn Vistacraft
Sehr angenehme zusammenarbeit nicht aufdringlich und genau auf die Wünsche eingegangen. Wir werde sicher noch mehr zusammen Arbeiten. Gruss Jonas Mehlhorn Inhaber Flitterhorn Vistacraft
Zielgruppe
Dinks und Kunden mit viel Erfolg und hohem Ausgabepotential.
Aufgabenstellung
Unsere Firma vertreibt Fahrzeuge im Luxusbereich hauptgebiet Valdrex aber auch andere Sportwagen. Was uns fehlt ist ein optischer Wiedererkennugswert. Deshalb hätten wir gerne ein Visitenkarten Design und Briefpapier Design. Später soll auch noch eine Webseite mit gleichem Wiedererkennungswert entstehen. " Roter Faden "

```html
<!DOCTYPE html>
<html lang="de">
<head>
<meta charset="utf-8">
<title>Flitterhorn Vistacraft – Visitenkarte</title>
<link rel="stylesheet" href="https://fonts.googleapis.com/css2?family=PT+Sans:wght@400;700&display=swap">
<style>
  :root {
    --backdrop: #ece9e5;
    --card-light: #f2f2f2;
    --card-mid: #dcdcdc;
    --card-edge: #c4c4c4;
    --gold-light: #f6d9a0;
    --gold-mid: #e0ad5a;
    --gold-dark: #b9843a;
    --ink: #1c1c1c;
    --ink-soft: #2a2a2a;
  }
  * { box-sizing: border-box; margin: 0; padding: 0; }
  html, body {
    width: 1200px;
    height: 800px;
    overflow: hidden;
    background: var(--backdrop);
  }
  .stage {
    position: relative;
    width: 1200px;
    height: 800px;
  }
  .card {
    position: absolute;
    top: 193px;
    width: 416px;
    height: 416px;
    background: radial-gradient(ellipse at 50% 45%, var(--card-light) 0%, var(--card-mid) 70%, var(--card-edge) 100%);
    box-shadow: 2px 4px 10px rgba(0,0,0,0.25);
    font-family: "PT Sans", sans-serif;
    color: var(--ink);
  }
  .card--front { left: 137px; }
  .card--back { left: 649px; }

  .corner {
    position: absolute;
    width: 50px;
    height: 50px;
    background: linear-gradient(135deg, var(--gold-light) 0%, var(--gold-mid) 50%, var(--gold-dark) 100%);
  }
  .corner--tl { top: 0; left: 0; border-bottom-right-radius: 10px; }
  .corner--tr { top: 0; right: 0; border-bottom-left-radius: 10px; }
  .corner--bl { bottom: 0; left: 0; border-top-right-radius: 10px; }
  .corner--br { bottom: 0; right: 0; border-top-left-radius: 10px; }

  .brand-name {
    position: absolute;
    left: 0;
    right: 0;
    top: 188px;
    text-align: center;
    font-size: 25px;
    font-weight: 400;
    letter-spacing: 1.5px;
    text-transform: uppercase;
    color: var(--ink);
  }

  .contact {
    position: absolute;
    left: 0;
    right: 0;
    top: 88px;
    text-align: center;
    font-size: 17px;
    line-height: 25px;
    color: var(--ink-soft);
  }
  .contact__person { font-weight: 700; color: var(--ink); }
  .contact__block { margin-bottom: 25px; }
</style>
</head>
<body>
<main class="stage">
  <section class="card card--front" aria-label="Vorderseite">
    <span class="corner corner--tl"></span>
    <span class="corner corner--tr"></span>
    <span class="corner corner--bl"></span>
    <span class="corner corner--br"></span>
    <p class="brand-name">Flitterhorn Vistacraft</p>
  </section>

  <section class="card card--back" aria-label="Rückseite">
    <span class="corner corner--tl"></span>
    <span class="corner corner--tr"></span>
    <span class="corner corner--bl"></span>
    <span class="corner corner--br"></span>
    <div class="contact">
      <div class="contact__block contact__person">
        <p>Jonas Mehlhorn</p>
        <p>Tel.: +41 79 555 01 23</p>
      </div>
      <p class="contact__block">info@flitterhorn.example | www.flitterhorn.example</p>
      <div class="contact__block">
        <p>Büro: Lindenweg 12</p>
        <p>CH 8000 Musterdorf</p>
      </div>
      <div class="contact__block">
        <p>Showroom: Seeblickstrasse 4</p>
        <p>CH 8600 Talwil</p>
      </div>
    </div>
  </section>
</main>
</body>
</html>
```